Gymnastics Award Design Needed--for kids

Need a gymnastics certificate or award designed. Will be printed on a piece of 8.5x11 paper. The award will be celebrating the gymnast learning a new skill in gymnastics. So it should be fun, but still look "official". Needs to look good hanging on a gymnast's bedroom wall.

It should say "The Aerial Cartwheel Club"
I will be using this design to change it based on the skill.

My main colors are:
#34475D
#E1467A
#7555A4

So should use those, but can add others

My website is tumblenestpro.com so you can see the look/feel.

Target Market(s)

Main audience will be girls ages 5-12, but will also be used by slightly older girls and boys. So needs to be fun, not too gender specific.

Industry/Entity Type

Learning

Requirements
Must have
• The following will need to go on the certificate:
• * Name of Skill
• * Image of Skill
• * Gymnast's Name
• * my logo
• * Gym's Logo
• * Gym's Name
• Optional: Date

```html
<!DOCTYPE html>
<html lang="en">
<head>
<meta charset="utf-8">
<title>Aerial Cartwheel Club Certificate</title>
<link href="https://fonts.googleapis.com/css2?family=Amaranth:wght@400;700&display=swap" rel="stylesheet">
<style>
  :root {
    --navy: #34475D;
    --pink: #E1467A;
    --purple: #7555A4;
    --purple-dark: #5a3f85;
    --cream: #e9e8cf;
    --cream-line: #d9d8bb;
    --paper: #ffffff;
    --grey-text: #6f6f6f;
    --backdrop: #ece6f1;
  }
  * { margin: 0; padding: 0; box-sizing: border-box; }
  html, body {
    width: 1200px;
    height: 1200px;
    overflow: hidden;
    background: var(--backdrop);
  }
  .canvas {
    position: relative;
    width: 1200px;
    height: 1200px;
  }
  .certificate {
    position: absolute;
    left: 50px;
    top: 176px;
    width: 1100px;
    height: 847px;
    display: block;
  }
  .frame-outer { fill: var(--pink); }
  .frame-navy { fill: var(--navy); }
  .frame-cream { fill: var(--cream); }
  .frame-line { fill: none; stroke: var(--cream-line); stroke-width: 2; }
  .panel { fill: var(--paper); }
  .ribbon-band { fill: var(--purple); }
  .ribbon-tail { fill: var(--purple); }
  .ribbon-fold { fill: var(--purple-dark); }
  .label {
    font-family: "Amaranth", sans-serif;
    font-weight: 700;
    fill: var(--purple);
  }
  .label-the { font-size: 26px; }
  .label-club { font-size: 27px; }
  .skill-title {
    font-family: "Amaranth", sans-serif;
    font-weight: 700;
    font-size: 60px;
    fill: #ffffff;
  }
  .presented {
    font-family: "Amaranth", sans-serif;
    font-weight: 700;
    font-size: 22px;
    fill: var(--grey-text);
  }
  .brand-name {
    font-family: "Amaranth", sans-serif;
    font-weight: 400;
    font-size: 30px;
    letter-spacing: 1px;
    fill: var(--pink);
  }
  .brand-dot { fill: var(--purple); }
</style>
</head>
<body>
<div class="canvas">
  <svg class="certificate" viewBox="0 0 896 690" xmlns="http://www.w3.org/2000/svg">
    <defs>
      <linearGradient id="gymnast-fill" x1="0" y1="0" x2="0" y2="1">
        <stop offset="0" stop-color="#eed9c8"/>
        <stop offset="1" stop-color="#c9c2dc"/>
      </linearGradient>
    </defs>

    <!-- Layered frame -->
    <rect class="frame-outer" x="0" y="0" width="896" height="690"/>
    <rect class="frame-navy" x="16" y="16" width="864" height="658"/>
    <rect class="frame-cream" x="34" y="32" width="828" height="626"/>
    <rect class="frame-line" x="62" y="58" width="772" height="574" rx="6"/>
    <rect class="panel" x="83" y="78" width="730" height="530"/>

    <!-- Brand mark -->
    <g class="brand">
      <circle class="brand-dot" cx="492" cy="122" r="13"/>
      <text class="brand-name" x="514" y="133">TUMBLENEST PRO</text>
    </g>

    <!-- Title ribbon -->
    <g class="ribbon">
      <polygon class="ribbon-tail" points="83,222 12,222 30,276 12,330 83,330"/>
      <polygon class="ribbon-tail" points="813,222 884,222 866,276 884,330 813,330"/>
      <polygon class="ribbon-fold" points="76,302 83,330 83,302"/>
      <polygon class="ribbon-fold" points="820,302 813,330 813,302"/>
      <rect class="ribbon-band" x="76" y="192" width="744" height="110"/>
    </g>

    <text class="label label-the" x="148" y="178">The</text>
    <text class="skill-title" x="448" y="266" text-anchor="middle">Aerial Cartwheel</text>
    <text class="label label-club" x="770" y="340" text-anchor="end">Club</text>

    <text class="presented" x="150" y="404">Presented to</text>

    <!-- Skill illustrations -->
    <rect x="98" y="438" width="127" height="154" rx="10" fill="url(#gymnast-fill)"
          role="img" aria-label="Illustration of a gymnast performing an aerial cartwheel"/>
    <rect x="683" y="438" width="112" height="147" rx="10" fill="url(#gymnast-fill)"
          role="img" aria-label="Illustration of a gymnast in a back walkover"/>
  </svg>
</div>
</body>
</html>
```